Business Card for Consulting Company

I would need a business card for my consulting company - the company brand and logos are defined and shared as part of this project. The proposed design for the business card can be reused as inspiration for my email signature.

```html
<!DOCTYPE html>
<html lang="en">
<head>
<meta charset="utf-8">
<title>Arbora Consult – Business Card</title>
<link href="https://fonts.googleapis.com/css2?family=Open+Sans:wght@400;600;700&display=swap" rel="stylesheet">
<style>
  :root {
    --teal: #0aa9a6;
    --ink: #333333;
    --text: #3a3a3a;
    --paper: #ffffff;
    --backdrop: #e9e6e4;
    --rule: #c9c9c9;
  }
  * { margin: 0; padding: 0; box-sizing: border-box; }
  html, body {
    width: 1200px; height: 997px; overflow: hidden;
    background: var(--backdrop);
    font-family: "Open Sans", Arial, sans-serif;
  }
  .sheet {
    width: 1200px; height: 997px;
    display: flex; align-items: center; justify-content: center; gap: 60px;
  }
  .card {
    position: relative;
    width: 520px; height: 318px;
    background: var(--paper);
    box-shadow: 0 2px 6px rgba(0,0,0,.12);
    overflow: hidden;
  }
  /* front */
  .brand {
    position: absolute; left: 34px; top: 92px; width: 200px;
    display: flex; align-items: center; gap: 10px;
  }
  .brand-dot { width: 22px; height: 22px; border-radius: 50%; background: var(--teal); flex: none; }
  .brand-name { font-size: 22px; font-weight: 700; color: var(--teal); line-height: 1.15; }
  .divider {
    position: absolute; left: 258px; top: 52px; width: 1px; height: 128px;
    background: var(--rule);
  }
  .contact { position: absolute; left: 276px; top: 50px; color: var(--text); }
  .person-name { font-size: 17px; font-weight: 700; color: var(--teal); line-height: 1.2; }
  .person-role { font-size: 12px; margin-bottom: 14px; }
  .contact-list { list-style: none; font-size: 12.5px; }
  .contact-list li { display: flex; align-items: center; gap: 8px; line-height: 19px; }
  .contact-list svg { width: 12px; height: 12px; fill: var(--teal); flex: none; }
  .rule-dark {
    position: absolute; left: 0; right: 0; top: 214px; height: 3px; background: var(--ink);
  }
  .band-teal {
    position: absolute; left: 0; right: 0; top: 222px; height: 30px; background: var(--teal);
  }
  /* back */
  .back-mark {
    position: absolute; left: 0; right: 0; top: 100px;
    display: flex; justify-content: center; align-items: center; gap: 12px;
  }
  .back-mark .brand-dot { width: 28px; height: 28px; }
  .back-mark .brand-name { font-size: 28px; }
  .back-url {
    position: absolute; left: 0; right: 0; top: 214px; text-align: center;
    font-size: 15px; font-weight: 600; color: var(--ink);
  }
  .back-url .accent { color: var(--teal); }
</style>
</head>
<body>
<main class="sheet">
  <section class="card card-front">
    <div class="brand">
      <span class="brand-dot"></span>
      <span class="brand-name">Arbora Consult</span>
    </div>
    <div class="divider"></div>
    <div class="contact">
      <p class="person-name">Mathis Verlaine</p>
      <p class="person-role">Founder &amp; CEO</p>
      <ul class="contact-list">
        <li>
          <svg viewBox="0 0 24 24"><path d="M6.6 10.8a15.1 15.1 0 0 0 6.6 6.6l2.2-2.2c.3-.3.7-.4 1-.2 1.1.4 2.3.6 3.6.6.6 0 1 .4 1 1V20c0 .6-.4 1-1 1A17 17 0 0 1 3 4c0-.6.4-1 1-1h3.5c.6 0 1 .4 1 1 0 1.3.2 2.5.6 3.6.1.3 0 .7-.2 1z"/></svg>
          +41 79 000 12 34
        </li>
        <li>
          <svg viewBox="0 0 24 24"><path d="M2 5h20v14H2z M2 5l10 8 10-8" fill="none" stroke="#0aa9a6" stroke-width="2.4"/></svg>
          mathis.v@arboraconsult.ch
        </li>
        <li>
          <svg viewBox="0 0 24 24"><circle cx="12" cy="12" r="9.5" fill="none" stroke="#0aa9a6" stroke-width="2.2"/><path d="M2.5 12h19M12 2.5c3 3 3 16 0 19M12 2.5c-3 3-3 16 0 19" fill="none" stroke="#0aa9a6" stroke-width="1.8"/></svg>
          www.arboraconsult.ch
        </li>
      </ul>
    </div>
    <div class="rule-dark"></div>
    <div class="band-teal"></div>
  </section>

  <section class="card card-back">
    <div class="back-mark">
      <span class="brand-dot"></span>
      <span class="brand-name">Arbora Consult</span>
    </div>
    <p class="back-url">www.<span class="accent">arboraconsult</span>.ch</p>
  </section>
</main>
</body>
</html>
```